Log In Screen Design

We have an existing website (www.velmarix4.com) and have recently developed software which requires a login screen using a similar theme from the velmarix4 website. The login screen should have a username and password. The software title is Tiered Outcome Scheduling (TOS). The VELMARIX4 log should appear on the login screen and the page should look professional.
Target Market(s)
Project Management Professionals
Industry/Entity Type
Software
Requirements
Must have
- Username and password blocks
Company Logo
Company Name - VELMARIX4 Management Ltd
Software Name - Tiered Outcome Scheduling (TOS)
Similar theme (colors) to the logo and existing website

```html
<!DOCTYPE html>
<html lang="en">
<head>
<meta charset="utf-8">
<title>Tiered Outcome Scheduling – Login</title>
<link href="https://fonts.googleapis.com/css2?family=Source+Sans+3:wght@400;600;700&display=swap" rel="stylesheet">
<style>
  :root {
    --brand-blue: #2a7fc0;
    --top-bar: #1f74b8;
    --header-bg: #efefef;
    --text-grey: #666666;
    --name-grey: #6b6b6b;
    --field-bg: #e8e8e8;
    --card-border: #bdbdbd;
    --footer-bg: #efefef;
    --footer-line: #c9c9c9;
    --body-top: #9b9b9b;
    --body-bottom: #ececec;
  }
  * { margin: 0; padding: 0; box-sizing: border-box; }
  html, body { width: 1200px; height: 862px; overflow: hidden; }
  body {
    position: relative;
    font-family: "Source Sans 3", "Myriad Pro", Arial, sans-serif;
    background: linear-gradient(to bottom, var(--body-top) 168px, #c8c8c8 420px, var(--body-bottom) 720px, var(--body-bottom) 762px);
  }
  .top-bar { position: absolute; left: 0; top: 0; width: 1200px; height: 7px; background: var(--top-bar); }
  .site-header {
    position: absolute; left: 0; top: 7px; width: 1200px; height: 157px;
    background: var(--header-bg); border-bottom: 4px solid #ffffff;
  }
  .company-name {
    position: absolute; left: 268px; top: 52px; width: 600px;
    text-align: center; white-space: nowrap;
    font-size: 42px; font-weight: 600; line-height: 1;
    color: var(--name-grey);
  }

  .login-card {
    position: absolute; left: 244px; top: 205px; width: 712px; height: 472px;
    background: #ffffff; border: 2px solid var(--card-border); border-radius: 5px;
    box-shadow: 0 14px 14px -8px rgba(0,0,0,0.25);
  }
  .login-title {
    position: absolute; left: 145px; top: 26px;
    font-size: 39px; font-weight: 400; color: var(--brand-blue); white-space: nowrap;
  }
  .field-label {
    position: absolute; left: 145px; font-size: 21px; font-weight: 700; color: var(--text-grey); letter-spacing: 0.3px;
  }
  .label-username { top: 101px; }
  .label-password { top: 226px; }
  .field-input {
    position: absolute; left: 145px; width: 422px; height: 76px;
    background: var(--field-bg); border: none; outline: none;
    font-family: inherit; font-size: 22px; color: #444; padding: 0 18px;
  }
  .input-username { top: 132px; }
  .input-password { top: 257px; }
  .login-button {
    position: absolute; left: 258px; top: 372px; width: 200px; height: 62px;
    border: 1px solid #222; border-radius: 4px;
    background: radial-gradient(ellipse at center, #6a6a6a 0%, #3a3a3a 60%, #222 100%);
    color: #ffffff; font-family: inherit; font-size: 32px; font-weight: 700; letter-spacing: 3px;
    cursor: pointer;
  }

  .site-footer {
    position: absolute; left: 0; top: 762px; width: 1200px; height: 100px;
    background: var(--footer-bg); border-top: 1px solid var(--footer-line);
  }
  .site-footer::after {
    content: ""; position: absolute; left: 0; bottom: 7px; width: 1200px; height: 1px; background: var(--footer-line);
  }
  .footer-nav {
    position: absolute; top: 17px; width: 100%; text-align: center;
    font-size: 15.5px; color: var(--text-grey); white-space: nowrap;
  }
  .footer-nav a { color: var(--text-grey); text-decoration: none; }
  .footer-nav .sep { margin: 0 7px; color: #999; }
  .copyright {
    position: absolute; top: 60px; width: 100%; text-align: center;
    font-size: 15px; color: var(--text-grey);
  }
</style>
</head>
<body>
  <div class="top-bar"></div>
  <header class="site-header">
    <p class="company-name">VELMARIX4 Management Ltd</p>
  </header>

  <main class="login-card">
    <h1 class="login-title">Tiered Outcome Scheduling</h1>
    <label class="field-label label-username" for="username">USERNAME</label>
    <input class="field-input input-username" id="username" type="text">
    <label class="field-label label-password" for="password">PASSWORD</label>
    <input class="field-input input-password" id="password" type="password">
    <button class="login-button" type="button">LOGIN</button>
  </main>

  <footer class="site-footer">
    <nav class="footer-nav">
      <a href="#">Home</a><span class="sep">|</span>
      <a href="#">About us</a><span class="sep">|</span>
      <a href="#">Contact us</a><span class="sep">|</span>
      <a href="#">Overview</a><span class="sep">|</span>
      <a href="#">Project Control</a><span class="sep">|</span>
      <a href="#">Contract Management</a><span class="sep">|</span>
      <a href="#">Specialist Services</a><span class="sep">|</span>
      <a href="#">Reference Projects</a>
    </nav>
    <p class="copyright">Copyright © 2012 www.velmarix4.com All rights reserved.</p>
  </footer>
</body>
</html>
```